Electrictrian Contractor Website Design

We are working with an electrical contractor in California called Crest Electric.

Some sites to use for content/competitors and inspiration:
https://tamrinwired.com
https://pravikdesk.surf/web/contractor/ (lots of contractor website designs we've approved and continue to show clients)

Thank you for taking the time to consider designing a website for us. We are web developers based in Stockton, CA, USA. Most of our projects go through the same process. Understanding this process may help you win a project with us. We custom-code all of our websites in-house. We don’t have any requirements as to what tools you use for your design, but we prefer Figma files. For any design that we label as four-stars, we send it to the client for review. The client picks the final design they want us to use. Once we complete this process, we will continue to show additional clients all the four-star sites and purchase them later. Your designs will have multiple chances to sell. For better chances of success, we ask that you follow these guidelines.

IMAGES:
If you use any images or icons in the design, we ask that you have a link to the asset so we can purchase the image/icon. Most of the designs we submit do not have the customer’s images on them unless they have some great images. Be creative; show us the feeling you are trying to portray with your image choices. Use any royalty-free site you choose. We subscribe to Quillo and mainly use their images, but we can purchase images outside of Quillo.

PLEASE NOTE: we will not submit designs to clients with watermarks on the images.

FONTS:
We ask that you identify the fonts used in the design. This can be done in a message if you want. We typically use Google Fonts and Quillo Fonts.

CONTENT:
We're always open to different content and ideas. We often submit designs with stock images so the client can see our vision. We typically take pictures after the website launch to use their images with our vision. Lorem Ipsum is fine for paragraphs, but we ask that you write the headers in correct English. We want to be able to show the vision and identify the sections of the website.

INSPIRATION:
We typically add a couple of links in the brief of websites we like to help you get started in your design.

REVISIONS:
We do not often ask for revisions of the designs unless we see something in the design that may not appeal to the client. If there are slight changes that we want to make, we do that in the development process.

FEEDBACK:
We rarely give feedback on designs during the design process. We are working on many website projects and do not have the time to provide feedback. We usually respond if your request is well thought out and asks specific questions, but a note asking “feedback, please” usually goes unanswered

```html
<!DOCTYPE html>
<html lang="en">
<head>
<meta charset="utf-8">
<title>Crest Electric – Electrical &amp; General Engineering</title>
<link href="https://fonts.googleapis.com/css2?family=Poppins:wght@400;500;600;700;800&family=Heebo:wght@400;500;600;700&display=swap" rel="stylesheet">
<style>
:root{
  --blue:#123f92;
  --blue-nav:#12357c;
  --navy:#14294f;
  --navy-footer:#0e2b5e;
  --yellow:#f8c51c;
  --yellow-bright:#f2e52c;
  --grey-bg:#e6e9ef;
  --text:#2b2f38;
  --muted:#5d6470;
  --white:#ffffff;
}
*{margin:0;padding:0;box-sizing:border-box}
html,body{width:1200px;height:4710px;overflow:hidden}
body{position:relative;background:var(--white);font-family:"Heebo",sans-serif;color:var(--text)}
.abs{position:absolute}
.heading{font-family:"Poppins",sans-serif;font-weight:800;color:var(--blue);line-height:1.1}
.label{font-size:14px;color:var(--muted);padding-left:14px;border-left:4px solid var(--yellow);line-height:18px}
.btn{display:flex;align-items:center;justify-content:center;font-family:"Poppins",sans-serif;font-weight:600;font-size:11px;letter-spacing:.3px;text-transform:uppercase;border-radius:3px}
.btn-yellow{background:var(--yellow);color:var(--blue);border:2px solid #fff3}
.btn-blue{background:var(--blue);color:#fff}

/* header */
.topbar{left:0;top:0;width:1200px;height:9px;background:var(--yellow)}
.brand{font-family:"Poppins",sans-serif;font-weight:600;color:var(--blue);text-align:center;letter-spacing:6px;line-height:1}
.brand .b1{font-size:28px;display:block}
.brand .b2{font-size:26px;display:block;margin-top:4px}
.contact{display:flex;align-items:center;gap:12px}
.contact .ic{width:42px;height:42px;border-radius:50%;background:var(--yellow);display:flex;align-items:center;justify-content:center}
.contact small{display:block;font-size:11px;color:var(--muted)}
.contact strong{display:block;font-size:17px;font-weight:500;color:var(--blue)}
.search{left:1081px;top:35px;width:44px;height:44px;border-radius:50%;background:var(--blue);display:flex;align-items:center;justify-content:center}
.nav{left:31px;top:108px;width:1136px;height:46px;background:var(--blue-nav);display:flex;align-items:center;z-index:3}
.nav a{color:#fff;text-decoration:none;font-size:12.5px;text-transform:uppercase;margin-left:40px}
.nav a:first-child{color:var(--yellow);margin-left:40px}
.nav .quote{position:absolute;right:0;top:0;height:46px;width:156px;background:var(--yellow);color:var(--blue);font-weight:600;display:flex;align-items:center;justify-content:center;margin:0}

/* hero */
.hero{left:0;top:108px;width:1200px;height:604px;background:linear-gradient(90deg,#e9e8e6 0%,#dcdad6 45%,#8d8f92 60%,#6c6f73 80%,#50473f 100%)}
.hero-intro{left:68px;top:330px;font-family:"Poppins",sans-serif;font-size:29px;color:#222}
.hero-title{left:66px;top:372px;font-size:55px}
.hero-title .amp{color:var(--yellow)}
.hero-btn{left:68px;top:511px;width:119px;height:33px;font-size:11px}

/* about */
.about-back{left:185px;top:807px;width:366px;height:601px;background:linear-gradient(160deg,#9ea3a7,#5e6c7a 50%,#33475e)}
.about-frame{left:60px;top:900px;width:339px;height:402px;background:#fff;box-shadow:0 6px 24px #0002}
.about-front{left:79px;top:918px;width:301px;height:366px;background:linear-gradient(150deg,#aab0b5,#6f7f8f 55%,#3a4c5f)}
.years{left:60px;top:1316px;width:120px;text-align:center}
.years b{font-family:"Poppins",sans-serif;font-size:52px;font-weight:800;color:var(--yellow);line-height:1}
.years span{display:block;font-size:14px;color:var(--text);line-height:20px}
.about-label{left:627px;top:848px}
.about-title{left:627px;top:888px;font-size:37px}
.about-text{left:627px;top:1028px;width:480px;font-size:12.5px;line-height:25px;color:var(--muted)}
.features{left:627px;top:1140px;width:490px;display:flex}
.feature{flex:1;text-align:center;border-left:1px solid #d9dce2;padding-top:2px}
.feature:first-child{border-left:0}
.feature p{font-size:14.5px;font-weight:500;color:var(--blue);line-height:21px;margin-top:10px}
.about-btn{left:627px;top:1312px;width:128px;height:38px;font-size:11px}

/* services */
.services{left:0;top:1505px;width:1200px;height:686px;background:radial-gradient(ellipse at 50% 40%,#2a4b7a 0%,#1a3158 45%,#111f3c 100%)}
.services-label{left:46px;top:1708px;color:#dfe5ef;border-color:var(--yellow)}
.services-title{left:46px;top:1745px;font-size:37px;color:var(--yellow)}
.services-text{left:55px;top:1815px;width:480px;font-size:12.5px;line-height:26.5px;color:#e8ecf3}
.svc{width:280px;display:flex;gap:20px}
.svc .ic{flex:none;width:62px;height:62px;border-radius:50%;background:var(--yellow);display:flex;align-items:center;justify-content:center;margin-top:12px}
.svc h3{font-family:"Heebo",sans-serif;font-size:17px;font-weight:500;color:#fff;text-transform:uppercase;line-height:22px}
.svc p{font-size:12.5px;line-height:21px;color:#dfe4ec;text-align:justify;margin-top:4px;width:182px}
.svc a{display:block;font-size:10.5px;color:#fff;text-decoration:underline;margin-top:10px}

/* projects */
.projects{left:0;top:2191px;width:1200px;height:671px;background:linear-gradient(180deg,#dfe3ea,#e7eaf0)}
.proj-label{left:68px;top:2280px}
.proj-title{left:68px;top:2316px;font-size:37px}
.arrow-btn{width:42px;height:42px;border-radius:50%;border:1.5px solid #b5bcc8;display:flex;align-items:center;justify-content:center}
.card{top:2425px;width:233px;height:256px}
.card-overlay{position:absolute;inset:0;background:#1a3d7ccc;padding:0 12px 70px;display:flex;flex-direction:column;justify-content:flex-end}
.card-overlay small{color:var(--yellow);font-size:12px;font-weight:600}
.card-overlay strong{color:#fff;font-family:"Poppins",sans-serif;font-size:14.5px;font-weight:700;margin-top:2px}

/* CTA */
.cta{left:101px;top:2776px;width:1007px;height:176px;border-radius:6px;overflow:hidden;background:linear-gradient(180deg,#f6c51d,#e8b210);box-shadow:0 10px 26px #0002}
.cta-photo{position:absolute;right:0;top:0;width:410px;height:176px;clip-path:polygon(100px 0,410px 0,410px 176px,0 176px);background:linear-gradient(120deg,#0d2a4f,#2f5d8f 40%,#8b1e1e 70%,#1b2f4f)}
.cta-text{position:absolute;left:0;top:30px;width:650px;text-align:center;font-family:"Poppins",sans-serif;color:var(--blue)}
.cta-text .l1{font-size:33px;font-weight:500;line-height:40px}
.cta-text .l2{font-size:25px;font-weight:500;color:#fff;line-height:32px}
.cta-btn{position:absolute;left:250px;top:125px;width:152px;height:31px;font-size:12px}

/* clients */
.clients-label{left:68px;top:3046px}
.clients-title{left:68px;top:3082px;font-size:37px}
.client{width:180px;text-align:center;font-family:"Poppins",sans-serif;font-size:22px;font-weight:600;color:#8c9097;display:flex;align-items:center;justify-content:center;gap:10px}
.client i{width:14px;height:14px;border-radius:50%;background:#8c9097;display:block}

/* quote */
.quote-sec{left:0;top:3481px;width:1200px;height:674px;background:linear-gradient(180deg,#e9edf2,#e2e7ee)}
.quote-label{left:59px;top:3613px}
.quote-title{left:59px;top:3648px;font-size:37px}
.avatar{left:64px;top:3768px;width:75px;height:75px;border-radius:50%;background:linear-gradient(160deg,#c9ced6,#7d8896)}
.ask{left:165px;top:3776px}
.ask small{display:block;font-size:14px;color:var(--text)}
.ask strong{display:block;font-size:24px;font-weight:500;color:var(--blue);margin-top:4px}
.info{left:64px;font-size:18px;line-height:30px;color:var(--muted)}
.info b{font-weight:500;color:var(--text)}
.field{background:#fff;border:1px solid #d9dee6;border-radius:3px;font-size:16px;color:#6b717b;padding:0 24px;display:flex;align-items:center}
.textarea{align-items:flex-start;padding-top:18px}
.submit{left:561px;top:4000px;width:575px;height:60px;border-radius:4px;background:linear-gradient(90deg,#1c54b8,#2b3fc4);color:#fff;font-size:14px;gap:8px}

/* testimonial */
.testi{left:0;top:4155px;width:1200px;height:372px;background:var(--yellow-bright)}
.qmark{left:0;width:1200px;top:4196px;text-align:center;font-family:"Poppins",sans-serif;font-size:60px;font-weight:700;color:var(--navy);line-height:1}
.testi-text{left:270px;width:660px;top:4282px;text-align:center;font-size:14px;font-style:italic;line-height:22px;color:#3b3b3b}
.testi-name{left:0;width:1200px;top:4352px;text-align:center;font-size:14px;font-weight:600;color:#111}
.testi-role{left:0;width:1200px;top:4376px;text-align:center;font-size:12px;color:#555}
.t-avatar{border-radius:50%;background:linear-gradient(160deg,#d7b392,#8a6a52);border:3px solid #fff}

/* footer */
.footer{left:0;top:4527px;width:1200px;height:183px;background:var(--navy-footer)}
.footer-links{left:0;width:1200px;top:4634px;display:flex;justify-content:center;gap:26px}
.footer-links a{color:#fff;text-decoration:none;font-size:12px}
.copy{left:30px;top:4680px;font-size:11px;color:#cfd6e2}
.socials{left:1030px;top:4677px;display:flex;gap:16px}
.socials span{width:22px;height:22px;border-radius:50%;background:#24437a;display:block}
</style>
</head>
<body>

<!-- Header -->
<div class="abs topbar"></div>
<div class="abs brand" style="left:40px;top:27px;width:190px">
  <span class="b1">CREST</span><span class="b2">ELECTRIC</span>
</div>
<div class="abs contact" style="left:589px;top:36px">
  <span class="ic"><svg width="20" height="20" viewBox="0 0 24 24" fill="none" stroke="#12357c" stroke-width="1.8"><path d="M5 3h4l2 5-3 2a12 12 0 0 0 6 6l2-3 5 2v4a2 2 0 0 1-2 2A17 17 0 0 1 3 5a2 2 0 0 1 2-2z"/></svg></span>
  <div><small>Call Us Now</small><strong>(+1) 209 555 0148</strong></div>
</div>
<div class="abs contact" style="left:803px;top:36px">
  <span class="ic"><svg width="20" height="20" viewBox="0 0 24 24" fill="none" stroke="#12357c" stroke-width="1.8"><rect x="3" y="5" width="18" height="14" rx="2"/><path d="M3 7l9 6 9-6"/></svg></span>
  <div><small>Email Address</small><strong>support@crestmail.com</strong></div>
</div>
<div class="abs search"><svg width="16" height="16" viewBox="0 0 24 24" fill="none" stroke="#fff" stroke-width="2.6"><circle cx="10" cy="10" r="7"/><path d="M15 15l6 6"/></svg></div>

<!-- Hero -->
<div class="abs hero" role="img" aria-label="Photo of an electrician in a hard hat working on a circuit breaker panel"></div>
<nav class="abs nav">
  <a href="#">Home</a><a href="#">About</a><a href="#">Services</a><a href="#">Project</a><a href="#">Capabilities</a><a href="#">Careers</a><a href="#">Community</a><a href="#">Testimonials</a><a href="#">Contact</a>
  <a href="#" class="quote">Request a Quote</a>
</nav>
<p class="abs hero-intro">Reliability, Quality and Expertise in</p>
<h1 class="abs heading hero-title">Electrical <span class="amp">&amp;</span> General<br>Engineering</h1>
<a class="abs btn btn-yellow hero-btn">Know More</a>

<!-- About -->
<div class="abs about-back" role="img" aria-label="Photo of a distribution panel with coloured wiring"></div>
<div class="abs about-frame"></div>
<div class="abs about-front" role="img" aria-label="Photo of an electrician testing a panel with a multimeter"></div>
<div class="abs years"><b>20+</b><span>Years Of<br>Experience</span></div>
<p class="abs label about-label">Welcome To Crest Electric</p>
<h2 class="abs heading about-title">Best Electrical Solutions<br>For Your Electrical<br>Problems</h2>
<p class="abs about-text">Lorem ipsum dolor sit amet, consectetur adipiscing elit, sed do eiusmod tempor incididunt ut labore et dolore magna aliqua. Ut enim ad minim veniam, quis nostrud exercitation ullamco laboris nisi</p>
<div class="abs features">
  <div class="feature">
    <svg width="60" height="56" viewBox="0 0 60 56" fill="none" stroke="#f8c51c" stroke-width="2"><circle cx="33" cy="30" r="18"/><path d="M33 8v4M28 6h10M25 30l6 6 10-12M4 24h10M2 32h10M6 40h10"/></svg>
    <p>Rapid<br>Response</p>
  </div>
  <div class="feature">
    <svg width="60" height="56" viewBox="0 0 60 56" fill="none" stroke="#f8c51c" stroke-width="2"><path d="M22 8h20l8 10-18 22L14 18z M14 18h36M26 18l6 22 6-22M22 8l4 10 6-10 6 10 4-10"/><path d="M4 40c8-2 14 6 22 4l14-4"/></svg>
    <p>Premium<br>Service</p>
  </div>
  <div class="feature">
    <svg width="60" height="56" viewBox="0 0 60 56" fill="none" stroke="#f8c51c" stroke-width="2"><path d="M30 4l3 7 7 1-5 5 1 7-6-3-6 3 1-7-5-5 7-1z"/><path d="M14 14l2 4M46 14l-2 4M22 46V30a4 4 0 0 1 8 0v8h8a4 4 0 0 1 4 4v8H24z"/></svg>
    <p>5 Star<br>Rated</p>
  </div>
  <div class="feature">
    <svg width="60" height="56" viewBox="0 0 60 56" fill="none" stroke="#f8c51c" stroke-width="2"><path d="M30 6h20v20L26 50 6 30z"/><circle cx="42" cy="14" r="3"/><path d="M22 32l4 4 8-10"/></svg>
    <p>Best Offer<br>Guatanteed</p>
  </div>
</div>
<a class="abs btn btn-blue about-btn">Know More</a>

<!-- Services -->
<div class="abs services" role="img" aria-label="Night photo of a city skyline with lightning over the water"></div>
<p class="abs label services-label">Our Services</p>
<h2 class="abs heading services-title">What Service We Offer</h2>
<p class="abs services-text">Lorem ipsum dolor sit amet, consectetur adipiscing elit, sed do eiusmod tempor incididunt ut labore et dolore magna aliqua. Quis ipsum suspendisse ultrices gravida. Risus commodo viverra maecenas accumsan lacus vel facilisis. Lorem ipsum dolor sit amet, consectetur adipiscing elit, sed do eiusmod tempor incididunt ut labore et dolore magna aliqua. Ut enim ad minim veniam, quis nostrud exercitation ullamco laboris nisi ut aliquip ex ea commodo</p>

<div class="abs svc" style="left:575px;top:1631px">
  <span class="ic"><svg width="30" height="30" viewBox="0 0 30 30" fill="none" stroke="#1a3158" stroke-width="2"><path d="M15 3l10 4v7c0 7-5 11-10 13C10 25 5 21 5 14V7z"/><path d="M16 9l-4 7h5l-3 6"/></svg></span>
  <div><h3>Electrical Security</h3><p>Lorem ipsum dolor sit amet consect adipiscing elit, sed do eiusmod tempor incididunt</p><a>Know More</a></div>
</div>
<div class="abs svc" style="left:882px;top:1631px">
  <span class="ic"><svg width="30" height="30" viewBox="0 0 30 30" fill="none" stroke="#1a3158" stroke-width="2"><circle cx="15" cy="15" r="5"/><path d="M15 2v6M15 22v6M2 15h6M22 15h6M6 6l4 4M20 20l4 4M24 6l-4 4M10 20l-4 4"/></svg></span>
  <div><h3>Electricity Overuse</h3><p>Lorem ipsum dolor sit amet consect adipiscing elit, sed do eiusmod tempor incididunt</p><a>Know More</a></div>
</div>
<div class="abs svc" style="left:575px;top:1801px">
  <span class="ic"><svg width="30" height="30" viewBox="0 0 30 30" fill="none" stroke="#1a3158" stroke-width="2"><rect x="5" y="4" width="14" height="20" rx="2"/><path d="M9 24v4M15 24v4M19 12h6v10"/></svg></span>
  <div><h3>Faulty &amp; Old Wiring</h3><p>Lorem ipsum dolor sit amet consect adipiscing elit, sed do eiusmod tempor incididunt</p><a>Know More</a></div>
</div>
<div class="abs svc" style="left:882px;top:1801px">
  <span class="ic"><svg width="30" height="30" viewBox="0 0 30 30" fill="none" stroke="#1a3158" stroke-width="2"><circle cx="11" cy="11" r="6"/><path d="M15 15l10 10M20 4l4 4-4 4"/></svg></span>
  <div><h3>Install &amp; Upgrades</h3><p>Lorem ipsum dolor sit amet consect adipiscing elit, sed do eiusmod tempor incididunt</p><a>Know More</a></div>
</div>
<div class="abs svc" style="left:575px;top:1980px">
  <span class="ic"><svg width="30" height="30" viewBox="0 0 30 30" fill="none" stroke="#1a3158" stroke-width="2"><circle cx="15" cy="15" r="11"/><path d="M15 8v7l5 3"/></svg></span>
  <div><h3>Diagnosis &amp; Repair</h3><p>Lorem ipsum dolor sit amet consect adipiscing elit, sed do eiusmod tempor incididunt</p><a>Know More</a></div>
</div>
<div class="abs svc" style="left:882px;top:1980px">
  <span class="ic"><svg width="30" height="30" viewBox="0 0 30 30" fill="none" stroke="#1a3158" stroke-width="2"><rect x="6" y="3" width="6" height="10" rx="1"/><rect x="18" y="3" width="6" height="10" rx="1"/><path d="M9 13v14M21 13v14"/></svg></span>
  <div><h3>Cable Networking</h3><p>Lorem ipsum dolor sit amet consect adipiscing elit, sed do eiusmod tempor incididunt</p><a>Know More</a></div>
</div>

<!-- Projects -->
<div class="abs projects"></div>
<p class="abs label proj-label">Our Work</p>
<h2 class="abs heading proj-title">Explore Recent Projects</h2>
<div class="abs arrow-btn" style="left:989px;top:2270px"><svg width="12" height="12" viewBox="0 0 12 12" fill="none" stroke="#8d95a3" stroke-width="1.5"><path d="M8 2L4 6l4 4"/></svg></div>
<div class="abs arrow-btn" style="left:1049px;top:2270px"><svg width="12" height="12" viewBox="0 0 12 12" fill="none" stroke="#8d95a3" stroke-width="1.5"><path d="M4 2l4 4-4 4"/></svg></div>
<div class="abs card" style="left:68px;background:linear-gradient(180deg,#3d78c8,#7fb0e4 60%,#4a78b0)" role="img" aria-label="Photo of line workers on a utility pole against a blue sky"></div>
<div class="abs card" style="left:342px;background:linear-gradient(180deg,#4e6f96,#2b3f58)" role="img" aria-label="Photo of an industrial electrical site">
  <div class="card-overlay"><small>Project 2</small><strong>Work at Industry Area</strong></div>
</div>
<div class="abs card" style="left:622px;background:radial-gradient(circle at 40% 55%,#f3c269,#a86a2a 45%,#3b2412)" role="img" aria-label="Photo of hanging vintage pendant lights"></div>
<div class="abs card" style="left:896px;background:linear-gradient(120deg,#d9d6d0,#b9b4ac 55%,#3a3c40)" role="img" aria-label="Photo of an electrician testing a wall socket"></div>

<!-- CTA -->
<div class="abs cta">
  <div class="cta-photo" role="img" aria-label="Photo of colourful cable bundles in a server rack"></div>
  <div class="cta-text"><div class="l1">Need Any Help For</div><div class="l2">Electrical &amp; General Engineering Work?</div></div>
  <a class="btn btn-blue cta-btn">Contact Us</a>
</div>

<!-- Clients -->
<p class="abs label clients-label">We Worked For</p>
<h2 class="abs heading clients-title">Our Trusted Clients</h2>
<div class="abs client" style="left:23px;top:3195px"><i></i>Orvalo</div>
<div class="abs client" style="left:225px;top:3195px"><i></i>Strivane</div>
<div class="abs client" style="left:413px;top:3195px"><i></i>Keltrum</div>
<div class="abs client" style="left:590px;top:3195px"><i></i>Avrenta</div>
<div class="abs client" style="left:770px;top:3195px"><i></i>Slashwick</div>
<div class="abs client" style="left:953px;top:3195px"><i></i>Trivelle</div>
<div class="abs client" style="left:23px;top:3309px"><i></i>Corrano</div>
<div class="abs client" style="left:225px;top:3309px"><i></i>Linqsen</div>
<div class="abs client" style="left:413px;top:3309px"><i></i>Wudrel</div>
<div class="abs client" style="left:590px;top:3309px"><i></i>Sorvik</div>
<div class="abs client" style="left:770px;top:3309px"><i></i>Quadrel</div>
<div class="abs client" style="left:953px;top:3309px"><i></i>Hexlin</div>

<!-- Quote -->
<div class="abs quote-sec"></div>
<p class="abs label quote-label">Get A Quote</p>
<h2 class="abs heading quote-title">Get a Free Repair &amp;<br>Servicing Quote Now</h2>
<div class="abs avatar" role="img" aria-label="Portrait photo of a support agent with a headset"></div>
<div class="abs ask"><small>Have A Question</small><strong>(+1) 209 555 0148</strong></div>
<p class="abs info" style="top:3876px"><b>Monday - Friday</b><br>8.00 am - 7.00 pm / Sunday (Closed)</p>
<p class="abs info" style="top:3957px"><b>Ferrowick Company Inc.</b><br>1820, Halden Road, Lodi, CA 95240</p>
<div class="abs field" style="left:561px;top:3572px;width:280px;height:60px">Your Name</div>
<div class="abs field" style="left:857px;top:3572px;width:279px;height:60px">Phone</div>
<div class="abs field" style="left:561px;top:3654px;width:280px;height:61px">Email</div>
<div class="abs field" style="left:857px;top:3654px;width:279px;height:61px;justify-content:space-between">Service Option<svg width="12" height="8" viewBox="0 0 12 8"><path d="M0 0h12L6 8z" fill="#555"/></svg></div>
<div class="abs field textarea" style="left:561px;top:3737px;width:575px;height:232px">Message Here</div>
<a class="abs btn submit">Submit Now <svg width="18" height="18" viewBox="0 0 18 18" fill="none" stroke="#fff" stroke-width="1.6"><circle cx="9" cy="9" r="7.5"/><path d="M6 9h6M9.5 6.5L12 9l-2.5 2.5"/></svg></a>

<!-- Testimonial -->
<div class="abs testi"></div>
<div class="abs qmark">&rdquo;</div>
<p class="abs testi-text">Normal that has evolved from gene ration X is on the runway heading towards a streamlined cloud solution. strategies to ensure proactive domination.</p>
<div class="abs" style="left:60px;top:4334px"><svg width="24" height="20" viewBox="0 0 24 20" fill="none" stroke="#222" stroke-width="1.8"><path d="M22 10H3M10 3L3 10l7 7"/></svg></div>
<div class="abs" style="left:1108px;top:4334px"><svg width="24" height="20" viewBox="0 0 24 20" fill="none" stroke="#222" stroke-width="1.8"><path d="M2 10h19M14 3l7 7-7 7"/></svg></div>
<p class="abs testi-name">Dana Merrow</p>
<p class="abs testi-role">Fund manager</p>
<div class="abs t-avatar" style="left:480px;top:4419px;width:72px;height:72px" role="img" aria-label="Customer portrait photo"></div>
<div class="abs t-avatar" style="left:568px;top:4427px;width:56px;height:56px;background:linear-gradient(160deg,#e2c08e,#a57a45)" role="img" aria-label="Customer portrait photo"></div>
<div class="abs t-avatar" style="left:648px;top:4427px;width:56px;height:56px;background:linear-gradient(160deg,#e6d3c2,#9b7c66)" role="img" aria-label="Customer portrait photo"></div>

<!-- Footer -->
<div class="abs footer"></div>
<div class="abs brand" style="left:500px;top:4560px;width:200px;color:#fff"><span class="b1" style="font-size:24px">CREST</span><span class="b2" style="font-size:22px">ELECTRIC</span></div>
<nav class="abs footer-links"><a>Home</a><a>About</a><a>Services</a><a>Project</a><a>Capabilities</a><a>Careers</a><a>Community</a><a>Testimonials</a><a>Contact</a></nav>
<p class="abs copy">© Copyright 2024. All right reserved.</p>
<div class="abs socials" aria-label="Social links"><span></span><span></span><span></span><span></span></div>

</body>
</html>
```